Business Insurance for local SMEs (Small Medium Enterprises)

I am from Silver Harbour Wealth Planners (http://www.silverharbourwp.com.sg/shwp/index.html)
We need flyer design to penetrate into local market, to educate and advice business owners on Business Insurance. Areas like
- Business Succession
- Employee Benefit
- Corporate Business Insurance
Mainly is to deal with business risk management, minimise any potential business loss and thus, improving their business profit margin.

Target Market(s)

Local SME (Small Medium Enterprises) Business Owners

Industry/Entity Type

Business

Font styles to use
Serif

Colors
3377b5

Requirements
Must have
• Updates as of 31/March/2015-
• Its a 2-fold, A5 size brochure - please see attached for reference on the layout
• Please do include company logo (Planners' Circlet), as per attached.
Should not have
• Please remove Silver Harbour Wealth Planners Logo

```html
<!DOCTYPE html>
<html lang="en">
<head>
<meta charset="utf-8">
<title>Silver Harbour Wealth Planners – Business Insurance Flyer</title>
<link rel="stylesheet" href="https://fonts.googleapis.com/css2?family=Open+Sans:wght@400;600;700&display=swap">
<style>
  :root {
    --backdrop: #e6e9ec;
    --paper: #f4f5f6;
    --slate: #5d6a75;
    --slate-dark: #4a5661;
    --steel-blue: #7f9bb3;
    --tab-blue: #9cb3c6;
    --panel-grey: #6f777f;
    --footer-band: #a7bacb;
    --photo-light: #eef4f8;
    --photo-mid: #c9d8e3;
    --photo-deep: #8ea4b6;
    --white: #ffffff;
  }
  * { box-sizing: border-box; margin: 0; padding: 0; }
  html, body {
    width: 1200px;
    height: 800px;
    overflow: hidden;
    background: var(--backdrop);
    font-family: "Open Sans", Arial, sans-serif;
  }
  .flyer {
    position: absolute;
    left: 365px;
    top: 68px;
    width: 470px;
    height: 664px;
    background: var(--paper);
    box-shadow: 0 2px 10px rgba(0,0,0,0.15);
    overflow: hidden;
  }
  .hero-photo {
    position: absolute;
    left: 0; top: 0;
    width: 470px; height: 300px;
    background:
      radial-gradient(ellipse at 30% 55%, var(--photo-deep) 0%, rgba(142,164,182,0) 55%),
      linear-gradient(180deg, var(--photo-light) 0%, var(--photo-mid) 70%, #b8c7d3 100%);
  }
  .hero-swoosh {
    position: absolute;
    left: 0; top: 230px;
    width: 470px; height: 90px;
  }
  .headline {
    position: absolute;
    left: 178px; top: 18px;
    color: var(--slate);
  }
  .headline__kicker {
    font-size: 13px;
    font-weight: 400;
    letter-spacing: 0.3px;
  }
  .headline__main {
    font-size: 25px;
    font-weight: 600;
    line-height: 1.08;
    margin-top: 2px;
  }
  .intro {
    position: absolute;
    left: 18px; top: 310px;
    width: 240px;
    color: var(--slate);
  }
  .intro__lead {
    font-size: 12px;
    font-weight: 700;
    line-height: 1.3;
    color: var(--slate-dark);
  }
  .intro__text {
    font-size: 8.6px;
    line-height: 1.35;
    margin-top: 8px;
  }
  .brand {
    position: absolute;
    left: 262px; top: 324px;
    width: 196px;
    display: flex;
    align-items: center;
    gap: 8px;
  }
  .brand__mark {
    width: 14px; height: 14px;
    border-radius: 50%;
    background: var(--steel-blue);
    flex: none;
  }
  .brand__name {
    font-size: 15px;
    font-weight: 600;
    line-height: 1.1;
    color: var(--steel-blue);
  }
  .brand__group {
    position: absolute;
    left: 284px; top: 362px;
    font-size: 8.5px;
    font-weight: 600;
    color: var(--slate-dark);
  }
  .services {
    position: absolute;
    left: 16px; top: 422px;
    width: 438px;
    display: flex;
    gap: 12px;
  }
  .service {
    flex: 1;
    height: 192px;
    border-radius: 7px;
    overflow: hidden;
    background: var(--panel-grey);
  }
  .service__title {
    background: var(--tab-blue);
    color: var(--white);
    font-size: 8.4px;
    font-weight: 700;
    text-transform: uppercase;
    text-align: center;
    line-height: 1.15;
    height: 26px;
    display: flex;
    align-items: center;
    justify-content: center;
    padding: 0 6px;
  }
  .service__body {
    padding: 7px 8px;
    color: #eef1f3;
    font-size: 7.2px;
    line-height: 1.25;
  }
  .service__body p + p { margin-top: 6px; }
  .contact-band {
    position: absolute;
    left: 0; top: 622px;
    width: 470px; height: 24px;
    background: var(--footer-band);
    color: var(--white);
    font-size: 8.6px;
    display: flex;
    align-items: center;
    padding-left: 14px;
    gap: 3px;
  }
  .contact-band strong { font-weight: 700; }
</style>
</head>
<body>
  <article class="flyer">
    <div class="hero-photo" role="img" aria-label="Photo of a relaxed businessman in a grey suit seen from behind, hands clasped behind his head, in a bright office"></div>

    <svg class="hero-swoosh" viewBox="0 0 470 90" preserveAspectRatio="none" aria-hidden="true">
      <path d="M0 40 C120 10 250 70 470 30 L470 90 L0 90 Z" fill="#f4f5f6"/>
      <path d="M0 40 C120 10 250 70 470 30" fill="none" stroke="#9aa9b5" stroke-width="4" opacity="0.8"/>
      <path d="M0 52 C140 25 260 80 470 42" fill="none" stroke="#c3ccd3" stroke-width="2"/>
    </svg>

    <header class="headline">
      <p class="headline__kicker">UNDERSTANDING BUSINESSES</p>
      <h1 class="headline__main">PUTTING MINDS<br>AT EASE.</h1>
    </header>

    <section class="intro">
      <h2 class="intro__lead">Let us shoulder the unpredictability of non-business risks for you.</h2>
      <p class="intro__text">Keep your business on its current track of success or grow it even further, all while keeping your assets protected.</p>
      <p class="intro__text">Whether it is your employees or inventory, we know how important assets are to any successful company.</p>
    </section>

    <div class="brand">
      <span class="brand__mark"></span>
      <span class="brand__name">Silver Harbour Wealth Planners</span>
    </div>
    <p class="brand__group">A member of the Harbourline Group</p>

    <section class="services">
      <div class="service">
        <h3 class="service__title">Business<br>Succession</h3>
        <div class="service__body">
          <p>Business succession is a vital, yet often overlooked part of a long-term business strategy. We understand business. We know how important a good business succession plan is.</p>
          <p>Protect your business in the event of unexpected tragedies impacting key executives. Ensure the uninterrupted flow of business with cash compensations and be certain your business will survive its key employees.</p>
        </div>
      </div>
      <div class="service">
        <h3 class="service__title">Employee<br>Benefit</h3>
        <div class="service__body">
          <p>Hiring and retaining talent are keys to any organisation's success.</p>
          <p>An organisation that genuinely cares for its employees is one that will be appreciated by their talent, as employees know their well-being is being taken care of by their employer.</p>
          <p>Attract and retain dedicated talent to your company with employee benefits and see your company's existing talent nurture and grow within your organisation.</p>
        </div>
      </div>
      <div class="service">
        <h3 class="service__title">Commercial Business<br>Insurance</h3>
        <div class="service__body">
          <p>Protect your business against unexpected events such as theft, property damage and liability.</p>
          <p>Insure your business to ensure its future.</p>
          <p>Speak to a SHWP Consultant and safeguard the company you've worked hard to build up.</p>
        </div>
      </div>
    </section>

    <footer class="contact-band">
      HOTLINE <strong>(65) 6000 1234</strong> FAX <strong>(65) 6000 5678</strong> EMAIL <strong>contact_us@SilverHarbourWP.com.sg</strong>
    </footer>
  </article>
</body>
</html>
```